Business Intelligence/Analytics Technology Company Business Card

We are a higher-end enterprise software development company working with Retailer POS data to provide business intelligence and analytical services to fortune 500 companies.

I have an immediate need for a professional/thick/bold business card. The same design aspects will spiral into more media such as flyers/folders/etc...

Our website is www.brenvolq.com for our product.

I like "Clean" designs if that makes sense, not a lot of "stuff".

The uploaded files, the A logo with the box is the style we're leaning towards, but the A logo without the blue box is all good too... get creative.

Target Market(s)

Executives of large companies, down to VP level..

Industry/Entity Type

Software

Requirements
Must have
• I'm wanting a thick designer like business card.

I think we're going to change our logo to a more quillmesh 8 looking style... http://www.brenvolq.com/card.ai as an example of our current business card.

The winner will also have knowledge of where i can get these things printed.
Nice to have
• Blue-ish color scheme? I'm open to anything. Our Competition is Red, and another is Green. So we'll stick with the Blue.

```html
<!DOCTYPE html>
<html lang="en">
<head>
<meta charset="utf-8">
<title>Brenvolq Business Card</title>
<link rel="stylesheet" href="https://fonts.googleapis.com/css2?family=Open+Sans:wght@400;600&display=swap">
<style>
  :root {
    --blue-deep: #1f78b6;
    --blue-mid: #2790d2;
    --blue-edge: #2ea4ee;
    --band-top: #2e3437;
    --band-bottom: #1b2022;
    --ink: #17252d;
    --accent-red: #d40b0b;
    --white: #ffffff;
  }
  * { margin: 0; padding: 0; box-sizing: border-box; }
  html, body {
    width: 1200px;
    height: 720px;
    overflow: hidden;
  }
  body {
    font-family: "Open Sans", Arial, sans-serif;
  }
  .card {
    position: relative;
    width: 1200px;
    height: 720px;
    background: radial-gradient(ellipse 62% 58% at 50% 42%, var(--blue-deep) 0%, var(--blue-mid) 55%, var(--blue-edge) 100%);
  }
  .brand {
    position: absolute;
    left: 160px;
    top: 246px;
    display: flex;
    align-items: flex-end;
    gap: 40px;
  }
  .brand-square {
    width: 140px;
    height: 140px;
    background: var(--accent-red);
  }
  .brand-name {
    font-weight: 600;
    font-size: 84px;
    line-height: 1;
    letter-spacing: 18px;
    color: var(--ink);
    margin-bottom: -12px;
  }
  .band {
    position: absolute;
    top: 585px;
    height: 51px;
    background: linear-gradient(to bottom, var(--band-top), var(--band-bottom));
  }
  .band-left { left: 0; width: 187px; }
  .band-right { left: 1013px; width: 187px; }
  .band-center {
    left: 208px;
    width: 784px;
    display: flex;
    align-items: center;
    justify-content: center;
  }
  .website {
    color: var(--white);
    font-size: 23px;
    font-weight: 400;
    letter-spacing: 0.3px;
  }
</style>
</head>
<body>
  <main class="card">
    <div class="brand">
      <div class="brand-square"></div>
      <div class="brand-name">BRENVOLQ</div>
    </div>
    <div class="band band-left"></div>
    <div class="band band-center">
      <span class="website">www.brenvolq.com</span>
    </div>
    <div class="band band-right"></div>
  </main>
</body>
</html>
```